Sign Shop website

We need a web design for a sign company called Quillby Signs that builds signs for shops such as A Frames, Banners, Tennet Boards, Shop front windows etc...

The existing site is avaliable at www.quillbysigns.com.au

We will need to have a fresh makeover. The new site must have the following:

Photo Galleries (broken down into sections)
Store Locations (currently there are 4 stores)
Online quote form
List of services
About Us Page

We just need to front page designed in photoshop (the inner page is not necessary) We have a team that can code the site up.

The website should have the exact logo. Any person who alters the logo, design will be elimated.

No Twitter, RSS, LinkedIn icons

The main colours are yellow, black, blue, red

Target Market(s)

Any business

Industry/Entity Type

It Company

Requirements
Must have
• jQuery slider banner
Should not have
• Alter the logo in any way

```html
<!DOCTYPE html>
<html lang="en">
<head>
<meta charset="utf-8">
<title>Quillby Signs</title>
<link href="https://fonts.googleapis.com/css2?family=Open+Sans:wght@400;600;700;800&family=Oswald:wght@500;700&display=swap" rel="stylesheet">
<style>
:root{
  --red:#c62d12;
  --red-deep:#a61f08;
  --red-dark:#7d1505;
  --nav:#3a0b05;
  --cream:#fbf7ef;
  --ink:#2a1a14;
  --muted:#6d5a50;
  --link:#c77a10;
  --white:#ffffff;
  --yellow:#f2c21a;
}
*{margin:0;padding:0;box-sizing:border-box}
html,body{width:736px;height:1200px;overflow:hidden}
body{position:relative;background:var(--cream);font-family:"Open Sans",Arial,sans-serif;color:var(--ink)}
.hero-band{position:absolute;left:0;top:0;width:736px;height:345px;background:linear-gradient(180deg,#b52208 0%,#d9441c 45%,#e0582c 100%)}
.logo{position:absolute;left:105px;top:14px;display:flex;align-items:center;gap:10px}
.logo-mark{width:40px;height:40px;background:var(--yellow);border-radius:50%}
.logo-name{font-family:"Open Sans",Arial,sans-serif;font-weight:800;font-size:30px;color:var(--white)}
.top-links{position:absolute;left:420px;top:40px;font-size:8px;color:var(--white);display:flex;gap:14px}
.nav{position:absolute;left:105px;top:81px;width:530px;height:42px;background:var(--nav);display:flex;align-items:center;padding-left:8px}
.nav a{color:var(--white);text-decoration:none;font-size:12px;padding:0 18px;height:28px;line-height:28px}
.nav a.active{background:#5a1a10;border:1px solid #8a3a2a}
.slider{position:absolute;left:105px;top:135px;width:545px;height:195px;display:flex;overflow:hidden}
.slide{flex:1;position:relative}
.slide-photo{position:absolute;inset:0}
.s1 .slide-photo{background:linear-gradient(160deg,#d9b08f,#8a5a3c)}
.s2 .slide-photo{background:linear-gradient(160deg,#eae6e2,#8c8c90)}
.s3 .slide-photo{background:linear-gradient(160deg,#c9a184,#6e4b38)}
.s4 .slide-photo{background:linear-gradient(160deg,#b98a6c,#5a3a28)}
.s5 .slide-photo{background:linear-gradient(160deg,#d4a888,#7a5440)}
.caption{position:absolute;left:0;right:0;bottom:0;height:42px;background:rgba(20,8,4,.75);padding:4px 4px 0}
.caption h3{font-family:"Oswald",Arial,sans-serif;font-weight:500;font-size:21px;line-height:24px;color:var(--white);white-space:nowrap}
.caption span{display:block;font-size:7px;line-height:10px;color:#ff5a3a}
.section-title{font-size:11px;font-weight:700;color:var(--ink);text-transform:uppercase}
.services{position:absolute;left:105px;top:405px;width:220px}
.services ul{list-style:none;margin-top:16px}
.services li{font-size:8.5px;color:var(--link);line-height:14px}
.services li::before{content:"› ";color:var(--red)}
.btn{display:inline-block;background:var(--nav);color:var(--white);font-size:8px;padding:5px 10px;border-radius:2px}
.services .btn{position:absolute;top:170px;left:0}
.welcome{position:absolute;left:348px;top:405px;width:300px;height:200px}
.welcome p{font-size:8.5px;line-height:13px;color:var(--muted);margin-top:12px}
.welcome-img{position:absolute;left:25px;top:100px;width:44px;height:72px;background:linear-gradient(180deg,#d8d4ce,#6f6a64)}
.quote{position:absolute;left:105px;top:620px;width:545px;height:75px;background:var(--red);border:2px solid var(--red-dark);text-align:center;padding-top:8px}
.quote h2{font-family:"Oswald",Arial,sans-serif;font-weight:700;font-size:28px;line-height:32px;color:var(--white)}
.quote p{display:inline-block;background:#1a0603;color:var(--white);font-family:"Oswald",Arial,sans-serif;font-weight:500;font-size:17px;padding:0 8px;line-height:22px}
.about{position:absolute;left:105px;top:722px;width:170px}
.about p{font-size:8.5px;line-height:13px;color:var(--muted);margin-top:12px}
.about .btn{position:absolute;top:110px;left:0}
.galleries{position:absolute;left:294px;top:722px;width:345px}
.gallery-tiles{display:flex;gap:29px;margin-top:27px}
.tile{width:94px;height:47px;background:var(--red);border-radius:3px;display:flex;align-items:center;justify-content:center}
.footer{position:absolute;left:0;top:895px;width:736px;height:305px;background:linear-gradient(180deg,var(--red) 0%,var(--red-deep) 100%)}
.foot-col{position:absolute;top:20px;color:var(--white)}
.foot-col h4{font-size:10px;font-weight:700;margin-bottom:14px}
.foot-col p{font-size:7.5px;line-height:12px;color:#ffd9cf}
.form-field{width:130px;height:20px;background:var(--red-dark);border:1px solid #e06a4a;font-size:8px;color:var(--white);padding:3px 5px;margin-bottom:5px}
.form-field.area{height:70px}
.send{position:absolute;left:103px;top:166px;background:var(--nav);color:var(--white);font-size:7px;padding:3px 8px}
.copyright{position:absolute;left:105px;top:251px;width:545px;text-align:center;font-size:8px;color:var(--white);border-top:1px solid #d24a2a;padding-top:12px}
</style>
</head>
<body>
<div class="hero-band"></div>
<div class="logo"><span class="logo-mark"></span><span class="logo-name">Quillby Signs</span></div>
<div class="top-links"><span>Need Help? Call us on (02) 5550 1234</span><span>Log in</span><span>Register</span></div>
<nav class="nav"><a class="active">Home</a><a>About us</a><a>Services</a><a>Portfolio</a><a>Contact us</a></nav>

<section class="slider">
  <div class="slide s1"><div class="slide-photo" role="img" aria-label="Photo of a smiling business owner"></div><div class="caption"><h3>Starting Up</h3><span>Read More</span></div></div>
  <div class="slide s2"><div class="slide-photo" role="img" aria-label="Photo of a hand moving a chess piece"></div><div class="caption"><h3>Strategies</h3><span>Read More</span></div></div>
  <div class="slide s3"><div class="slide-photo" role="img" aria-label="Photo of a consultant at work"></div><div class="caption"><h3>Consulting</h3><span>Read More</span></div></div>
  <div class="slide s4"><div class="slide-photo" role="img" aria-label="Photo of a smiling developer"></div><div class="caption"><h3>Development</h3><span>Read More</span></div></div>
  <div class="slide s5"><div class="slide-photo" role="img" aria-label="Photo of a support team member"></div><div class="caption"><h3>24/7 Support</h3><span>Read More</span></div></div>
</section>

<section class="services">
  <h2 class="section-title">Services</h2>
  <ul>
    <li>Quality Stickers &amp; Decals</li>
    <li>A-Frame Signs</li>
    <li>Vehicle Signage</li>
    <li>Banners</li>
    <li>Construction Safety Signs</li>
    <li>Window Signage</li>
    <li>Lightboxes</li>
  </ul>
  <span class="btn">Read More</span>
</section>

<section class="welcome">
  <h2 class="section-title">Welcome</h2>
  <p>Quillby Signs is a locally owned sign company. We build signs for shops of every size, from a simple A-frame to full shop front windows, banners and lightboxes. Talk to our team today and let us help your business stand out.</p>
  <div class="welcome-img" role="img" aria-label="Photo of a printed shop sign"></div>
</section>

<section class="quote">
  <h2>Need a Quote</h2>
  <p>Request a quote online today</p>
</section>

<section class="about">
  <h2 class="section-title">About Us</h2>
  <p>Quillby Signs is a family owned and operated sign company. Started in 1995, we have grown to four stores and remain a trusted maker of quality signage.</p>
  <span class="btn">Read More</span>
</section>

<section class="galleries">
  <h2 class="section-title">Photo Galleries</h2>
  <div class="gallery-tiles">
    <div class="tile"><svg width="22" height="22" viewBox="0 0 24 24" fill="#fff"><circle cx="12" cy="12" r="7"/><circle cx="12" cy="12" r="3" fill="#c62d12"/><rect x="10.5" y="1" width="3" height="5"/><rect x="10.5" y="18" width="3" height="5"/><rect x="1" y="10.5" width="5" height="3"/><rect x="18" y="10.5" width="5" height="3"/></svg></div>
    <div class="tile"><svg width="26" height="20" viewBox="0 0 26 20" fill="#fff"><circle cx="13" cy="5" r="4"/><path d="M5 20c0-5 4-8 8-8s8 3 8 8z"/><circle cx="4" cy="7" r="3"/><circle cx="22" cy="7" r="3"/></svg></div>
    <div class="tile"><svg width="22" height="22" viewBox="0 0 24 24" fill="#fff"><circle cx="12" cy="12" r="7"/><circle cx="12" cy="12" r="3" fill="#c62d12"/><rect x="10.5" y="1" width="3" height="5"/><rect x="10.5" y="18" width="3" height="5"/><rect x="1" y="10.5" width="5" height="3"/><rect x="18" y="10.5" width="5" height="3"/></svg></div>
  </div>
</section>

<footer class="footer">
  <div class="foot-col" style="left:105px;width:110px">
    <h4>LATEST POSTS</h4>
    <p>New window range</p><br>
    <p>Unit 3, 18 Mill Road, Greenvale<br>Ph: (02) 5550 4411<br>Open Mon to Sat</p>
  </div>
  <div class="foot-col" style="left:245px;width:110px">
    <h4>OUR STORES</h4>
    <p>Greenvale</p><br>
    <p>Shop 5, 42 Park Promenade<br>Ph: (02) 5550 1234</p>
  </div>
  <div class="foot-col" style="left:385px;width:110px">
    <h4>TAGS</h4>
    <p>Banner Lane</p><br>
    <p>7/21 Larch Lane, Rosehill<br>Ph: (02) 5550 9876</p>
  </div>
  <div class="foot-col" style="left:527px">
    <h4>CONTACTS</h4>
    <div class="form-field">Username</div>
    <div class="form-field">Email</div>
    <div class="form-field area">Message</div>
    <span class="send">Send</span>
  </div>
  <div class="copyright">Quillby Signs © 2013 Privacy Policy</div>
</footer>
</body>
</html>
```